Marketing Flyer for Plumber Referals

8.5" x11" Layout should be landscape not portrait. Create a bold, eye-catching flyer that highlights earning potential from referrals for water damage restoration. Use high-contrast colors like blue, yellow, and white, with bold fonts and dynamic layouts. Include images of restoration work, cash, and happy clients. Emphasize key benefits like $500 minimum payouts, fast payments, and unlimited income potential. Keep instructions simple: refer a client, we handle the work, you get paid. Add a clear call-to-action and display contact details prominently. Focus on professionalism and energy.

Target Market(s)

Plumbers and Contractor 8.5" x11" Layout should be landscape not portrait.

Industry/Entity Type

General Contractor

Colors
0054AA
0677BA
7BADD7
CADEEF
E8F1F8
EB3D1F
EC4F4E
F09395
F8D3D4
FCEDEE

Requirements
Must have
• 8.5" x11" Layout should be landscape not portrait.
Nice to have

```html
<!DOCTYPE html>
<html lang="en">
<head>
<meta charset="utf-8">
<title>Referral Flyer – Harborline Renovation</title>
<link href="https://fonts.googleapis.com/css2?family=Montserrat:wght@500;600;700&family=Source+Sans+3:wght@400;600;700&display=swap" rel="stylesheet">
<style>
  :root {
    --stage: #bdbdbd;
    --paper: #ffffff;
    --ink: #0f2a4a;
    --ink-soft: #24405f;
    --blue-deep: #0054AA;
    --blue: #0677BA;
    --blue-mid: #7BADD7;
    --blue-light: #CADEEF;
    --blue-pale: #E8F1F8;
    --red: #EB3D1F;
    --red-soft: #EC4F4E;
  }
  * { margin: 0; padding: 0; box-sizing: border-box; }
  html, body { width: 1200px; height: 2254px; overflow: hidden; }
  body {
    background: var(--stage);
    position: relative;
    font-family: "Source Sans 3", Arial, sans-serif;
    color: var(--ink);
  }
  .page {
    position: absolute;
    left: 40px;
    width: 1120px;
    height: 865px;
    background: var(--paper);
    overflow: hidden;
  }
  .page--front { top: 232px; }
  .page--back { top: 1157px; }
  .heading { font-family: "Montserrat", Arial, sans-serif; position: absolute; white-space: nowrap; }

  /* front */
  .skyline-photo {
    position: absolute; left: 0; top: 0; width: 400px; height: 865px;
    background: linear-gradient(180deg, var(--blue-mid) 0%, var(--blue) 45%, var(--blue-deep) 70%, var(--blue) 100%);
  }
  .brand-block {
    position: absolute; left: 40px; top: 720px; width: 320px; height: 100px;
    background: var(--red); color: var(--paper);
    display: flex; flex-direction: column; align-items: center; justify-content: center;
    white-space: nowrap;
  }
  .brand-name { font-weight: 600; font-size: 22px; letter-spacing: 1px; }
  .brand-tag { font-weight: 600; font-size: 10px; letter-spacing: 3px; margin-top: 6px; text-transform: uppercase; }
  .front-title { left: 460px; top: 80px; font-size: 34px; font-weight: 600; line-height: 46px; }
  .front-title .hot { color: var(--red); }
  .payout { position: absolute; left: 460px; top: 222px; font-family: "Montserrat", sans-serif; font-weight: 700; white-space: nowrap; }
  .payout-amount { font-size: 54px; color: var(--red); }
  .payout-terms { font-size: 24px; margin-left: 8px; }
  .partner-line { position: absolute; left: 460px; top: 310px; font-size: 18px; color: var(--ink-soft); }
  .benefits-band { position: absolute; left: 400px; top: 370px; width: 720px; height: 270px; }
  .benefits-title { left: 460px; top: 394px; font-size: 32px; font-weight: 600; color: var(--paper); }
  .benefits-list { position: absolute; left: 460px; top: 456px; list-style: none; color: var(--paper); font-size: 15.5px; line-height: 30px; white-space: nowrap; }
  .benefits-list li::before { content: "• "; color: var(--blue-light); }
  .front-tagline { position: absolute; left: 460px; top: 700px; font-size: 26px; font-weight: 700; color: var(--red); }

  /* back */
  .title-block { position: absolute; left: 0; top: 0; width: 640px; height: 260px; background: var(--blue-deep); }
  .back-title { left: 60px; top: 60px; font-size: 60px; font-weight: 600; line-height: 74px; color: var(--paper); }
  .side-bar { position: absolute; left: 680px; top: 160px; width: 29px; height: 183px; background: var(--red-soft); }
  .steps-title { left: 60px; top: 310px; font-size: 37px; font-weight: 600; color: var(--blue-deep); }
  .steps { position: absolute; left: 60px; top: 385px; font-size: 19px; line-height: 28px; list-style: none; white-space: nowrap; }
  .step-name { font-weight: 700; }
  .step-name span { color: var(--red); }
  .step-detail { padding-left: 34px; color: var(--ink-soft); }
  .flood-photo {
    position: absolute; left: 0; top: 620px; width: 1120px; height: 245px;
    background: linear-gradient(180deg, var(--blue-pale) 0%, var(--blue-light) 35%, var(--blue-mid) 65%, var(--blue) 100%);
  }
  .contact-strip {
    position: absolute; left: 0; top: 780px; width: 1120px; height: 70px;
    background: rgba(0, 84, 170, 0.85); color: var(--paper);
    padding: 13px 0 0 60px; font-size: 18px; line-height: 22px;
  }
</style>
</head>
<body>
  <section class="page page--front">
    <div class="skyline-photo" role="img" aria-label="City skyline at dusk reflected across the bay"></div>
    <div class="brand-block">
      <span class="brand-name">HARBORLINE RENOVATION</span>
      <span class="brand-tag">Coastal Quality Builders</span>
    </div>
    <h1 class="heading front-title">EARN UNLIMITED CASH<br><span class="hot">GET PAID</span> TO REFER A FLOOD</h1>
    <p class="payout"><span class="payout-amount">$500</span><span class="payout-terms">Minimum or 10% Per Referral!</span></p>
    <p class="partner-line">Partner with the #1 Water Damage Restoration Team</p>
    <svg class="benefits-band" viewBox="0 0 720 270" aria-hidden="true">
      <polygon points="0,0 640,0 720,270 0,270" fill="#0054AA"/>
    </svg>
    <h2 class="heading benefits-title">WHY PARTNER WITH US?</h2>
    <ul class="benefits-list">
      <li>Guaranteed Payout: Minimum $500 or 10% of the invoice, paid fast.</li>
      <li>Free Evaluations: We assess damage and process insurance claims for your clients.</li>
      <li>Industry Leaders: Certified experts with 24/7 rapid response.</li>
      <li>Affordable Solutions: Lowest out-of-pocket costs for your customers.</li>
    </ul>
    <p class="front-tagline">Send Referrals. Get Paid. Grow Your Business.</p>
  </section>

  <section class="page page--back">
    <div class="title-block"></div>
    <h1 class="heading back-title">GET PAID TO<br>REFER A FLOOD</h1>
    <div class="side-bar"></div>
    <h2 class="heading steps-title">HOW IT WORKS</h2>
    <ol class="steps">
      <li class="step-name"><span>1.</span> Refer Flood, Water and Mold Damage</li>
      <li class="step-detail">o Call, book online, or text us directly.</li>
      <li class="step-name"><span>2.</span> We Take Care of Everything</li>
      <li class="step-detail">o Free evaluations, insurance claims, and professional service.</li>
      <li class="step-name"><span>3.</span> Get Paid Fast</li>
      <li class="step-detail">o $500 minimum or 10% of the invoice within 48 hours of final payment.</li>
    </ol>
    <div class="flood-photo" role="img" aria-label="Flooded home interior with water covering the floor at the foot of a staircase"></div>
    <div class="contact-strip">
      Call Text or Book On-line<br>555-014-7720 | HarborlineRenovation.com
    </div>
  </section>
</body>
</html>
```